Web Design Front Page Only for Organic Skincare

We have been in business for nearly 20 years. We are run by all females and sell anything from aromatherapy, skincare and pharmacy types products to health food shops and pharmacy. We are looking for an attractive and colourful but simple front web page design for our wholesale customers to look at. We want our customers to start using our website to find information rather than ringing us. So we want it to be attractive to our buyers who are young and funky.
Updates

To give you an idea of the products we sell to pharmacy and health food shops also beauty shops and hair salons.  We mainly deal with organic body and skincare, aromatherapy oils and body products, but also do some simple pharmacy products such as bandages and pill boxes, finger splits, walking frames and wheelchairs.  We are only looking for the front page of the website.  The back-end will be done in-house.  We currently do not have a logo designed so I am thinking that once we have done the website design we can build a logo from it.  I like bright colours and want something that is inviting to further discover that we do many different types of products.

Target Market(s)

young girls who are our retail buyers

Industry/Entity Type

Pharmacy

Requirements
Must have
• A section which says

Customer Log in
Should not have
• don't worry about too much writing or tabs. We will insert these later. Just come up with design image.

```html
<!DOCTYPE html>
<html lang="en">
<head>
<meta charset="utf-8">
<title>Verdella Wellness</title>
<link href="https://fonts.googleapis.com/css2?family=Raleway:wght@300&family=Roboto+Condensed:wght@700&family=Questrial&display=swap" rel="stylesheet">
<style>
  :root {
    --bg-top: #72d277;
    --bg-bottom: #b6f6b4;
    --panel: #4fad4f;
    --panel-active: #419c43;
    --footer: #379a3a;
    --product-bg: #b5f5b5;
    --white: #ffffff;
    --text-grey: #6b6b6b;
    --dots: rgba(255,255,255,0.55);
    --button-light: #8fdf91;
    --image-light: #f2f5f1;
    --image-shade: #dfe6dd;
  }
  * { margin: 0; padding: 0; box-sizing: border-box; }
  html, body { width: 1149px; height: 1200px; overflow: hidden; }
  body {
    background: linear-gradient(to bottom, var(--bg-top) 0, var(--bg-top) 950px, var(--bg-bottom) 1200px);
  }
  .page {
    position: relative;
    width: 1100px; height: 1149px;
    transform: scale(1.0445, 1.0444);
    transform-origin: 0 0;
  }
  .header-shade {
    position: absolute; left: 0; top: 226px; width: 1100px; height: 30px;
    background: linear-gradient(to bottom, rgba(60,150,60,0) 0, rgba(60,150,60,0.35) 100%);
  }
  .brand {
    position: absolute; left: 131px; top: 79px;
    font-family: "Raleway", sans-serif; font-weight: 300;
    font-size: 40px; letter-spacing: 5px; color: var(--white);
    white-space: nowrap;
  }
  .account {
    position: absolute; left: 758px; top: 84px; width: 210px; height: 34px;
    display: flex; box-shadow: 0 2px 3px rgba(0,0,0,0.15);
  }
  .account a {
    flex: 1; display: flex; align-items: center; justify-content: center;
    background: linear-gradient(to bottom, #a3e8a4, var(--button-light));
    color: var(--white); font-family: Arial, sans-serif; font-size: 14px;
    text-decoration: none;
  }
  .account a + a { border-left: 1px solid #79c97b; }
  .main-nav {
    position: absolute; left: 133px; top: 183px; width: 835px; height: 67px;
    background: var(--panel); display: flex;
  }
  .main-nav a {
    display: flex; align-items: center; justify-content: center;
    font-family: "Roboto Condensed", sans-serif; font-weight: 700; font-size: 18px;
    color: var(--white); text-decoration: none; position: relative;
  }
  .main-nav a + a::before {
    content: ""; position: absolute; left: 0; top: 12px; bottom: 12px;
    border-left: 1px dotted var(--dots);
  }
  .main-nav a.active { background: var(--panel-active); }
  .main-nav a.active::before, .main-nav a.active + a::before { display: none; }
  .banner {
    position: absolute; left: 133px; top: 250px; width: 835px; height: 127px;
    background: linear-gradient(100deg, #5b4aa8 0%, #6f8f4e 20%, #7a66c2 40%, #88a860 58%, #6c56b8 78%, #8aa86a 100%);
    box-shadow: 0 4px 10px rgba(0,0,0,0.3);
  }
  .category-nav {
    position: absolute; left: 133px; top: 411px; width: 266px; height: 362px;
    background: var(--panel); padding: 7px 16px 0;
  }
  .category-nav a {
    display: flex; align-items: center; justify-content: center; height: 50px;
    font-family: "Roboto Condensed", sans-serif; font-weight: 700; font-size: 18px;
    color: var(--white); text-decoration: none;
    border-bottom: 1px dotted var(--dots);
  }
  .category-nav a:last-child { border-bottom: none; }
  .products {
    position: absolute; left: 424px; top: 411px; width: 543px; height: 571px;
    background: var(--product-bg);
  }
  .row-divider {
    position: absolute; left: 14px; top: 294px; width: 517px;
    border-top: 1px dotted #6fa86f;
  }
  .product { position: absolute; width: 170px; }
  .product-image {
    display: block; margin-left: 30px; width: 82px; height: 168px;
    background: linear-gradient(to bottom, var(--image-light), var(--image-shade));
    border-radius: 3px;
  }
  .product-name {
    margin-top: 18px; font-family: "Questrial", sans-serif; font-size: 13px;
    color: var(--text-grey); white-space: nowrap;
  }
  .product-price {
    margin-top: 8px; font-family: "Questrial", sans-serif; font-size: 13px; color: #8a8a8a;
  }
  .add-to-bag {
    display: flex; align-items: center; justify-content: center;
    margin-top: 8px; width: 112px; height: 20px; background: var(--panel);
    font-family: "Questrial", sans-serif; font-size: 13px; color: var(--white);
    text-decoration: none;
  }
  .site-footer {
    position: absolute; left: 161px; top: 1056px; width: 779px; height: 56px;
    background: var(--footer);
    display: flex; align-items: center; justify-content: center;
    font-family: Arial, sans-serif; font-size: 10px; color: var(--white);
  }
  .site-footer a { color: var(--white); text-decoration: none; padding: 0 9px; }
  .site-footer a + a { border-left: 1px solid var(--white); }
</style>
</head>
<body>
<div class="page">
  <div class="header-shade"></div>

  <div class="brand">VERDELLA WELLNESS</div>

  <nav class="account" aria-label="Customer log in">
    <a href="#">Log in</a>
    <a href="#">Register</a>
  </nav>

  <nav class="main-nav">
    <a href="#" style="width:135px">ABOUT US</a>
    <a href="#" style="width:142px">HEALTH FOOD</a>
    <a href="#" class="active" style="width:123px">PHARMACY</a>
    <a href="#" style="width:156px">SUPERMARKET</a>
    <a href="#" style="width:114px">BEAUTY</a>
    <a href="#" style="width:165px">CONTACT US</a>
  </nav>

  <div class="banner" role="img" aria-label="Photo of purple flowers among green leaves"></div>

  <nav class="category-nav">
    <a href="#">FACE CARE</a>
    <a href="#">HAIR CARE</a>
    <a href="#">FRAGRANCE</a>
    <a href="#">BATH &amp; BODY</a>
    <a href="#">FACE CARE</a>
    <a href="#">HAIR CARE</a>
    <a href="#">FRAGRANCE</a>
  </nav>

  <section class="products">
    <article class="product" style="left:54px;top:15px">
      <span class="product-image" role="img" aria-label="Product photo"></span>
      <div class="product-name">PRECIOUS CREAM 50 ML</div>
      <div class="product-price">70$</div>
      <a href="#" class="add-to-bag">ADD TO BAG</a>
    </article>
    <article class="product" style="left:313px;top:15px">
      <span class="product-image" role="img" aria-label="Product photo"></span>
      <div class="product-name">PRECIOUS CREAM 50 ML</div>
      <div class="product-price">70$</div>
      <a href="#" class="add-to-bag">ADD TO BAG</a>
    </article>
    <div class="row-divider"></div>
    <article class="product" style="left:52px;top:305px">
      <span class="product-image" role="img" aria-label="Product photo"></span>
      <div class="product-name">PRECIOUS CREAM 50 ML</div>
      <div class="product-price">70$</div>
      <a href="#" class="add-to-bag">ADD TO BAG</a>
    </article>
    <article class="product" style="left:310px;top:305px">
      <span class="product-image" role="img" aria-label="Product photo"></span>
      <div class="product-name">PRECIOUS CREAM 50 ML</div>
      <div class="product-price">70$</div>
      <a href="#" class="add-to-bag">ADD TO BAG</a>
    </article>
  </section>

  <footer class="site-footer">
    <a href="#">About us</a>
    <a href="#">Health food</a>
    <a href="#">Pharmacy</a>
    <a href="#">Supermarket</a>
    <a href="#">Beauty</a>
    <a href="#">Contact us</a>
  </footer>
</div>
</body>
</html>
```